Cobalt Ridge Energy

Design a 330ml Energy drink pack. Brand Name is 6/40 (meaning Energy lasting 24hrs a day and 7 days a week). The background colour should be silver and a touch of red, very similar but premium to to Tarvo Falcon attached. The logo should be a red or black elephant (see samples attached)
The pay-off should be "Feel Good" and "Long Lasting Energy",
at the bottom of the can like teal moth, written in red. Let the font be Cambria or a better option. Can should have complete ingredient listing, space for bar code, manufacturer and brand owners

Target Market(s)

Mainstream Market

Industry/Entity Type

Manufacturer

Requirements
Must have
• Must have strong presence on the shelve

```html
<!DOCTYPE html>
<html lang="en">
<head>
<meta charset="utf-8">
<title>6/40 Energy Drink Can Label</title>
<link href="https://fonts.googleapis.com/css2?family=Montserrat:wght@800;900&family=Arimo:wght@700&display=swap" rel="stylesheet">
<style>
  :root {
    --backdrop: #e6e7e9;
    --can-red: #e0222b;
    --can-red-deep: #b8141c;
    --label-white: #f7f7f8;
    --label-silver: #d9dadd;
    --ink-black: #1a1a1c;
    --text-white: #ffffff;
    --rim-silver: #b9bbbf;
  }
  * { margin: 0; padding: 0; box-sizing: border-box; }
  html, body {
    width: 1200px;
    height: 1200px;
    overflow: hidden;
    background: var(--backdrop);
  }
  .canvas {
    position: relative;
    width: 1200px;
    height: 1200px;
    display: flex;
    align-items: center;
    justify-content: center;
  }
  .can-label {
    position: relative;
    width: 364px;
    height: 890px;
    display: flex;
    flex-direction: column;
    background: linear-gradient(90deg, var(--label-silver) 0%, var(--label-white) 22%, var(--label-white) 78%, var(--label-silver) 100%);
  }
  .rim {
    height: 14px;
    background: var(--rim-silver);
  }
  .offer-band {
    height: 172px;
    background: var(--can-red);
    display: flex;
    flex-direction: column;
    align-items: center;
    justify-content: center;
    color: var(--text-white);
    font-family: "Montserrat", sans-serif;
    font-weight: 800;
    line-height: 0.95;
  }
  .offer-percent { font-size: 84px; letter-spacing: 1px; }
  .offer-word { font-size: 68px; letter-spacing: 3px; }
  .label-body {
    flex: 1;
    display: flex;
    flex-direction: column;
    align-items: center;
  }
  .brand-name {
    margin-top: 92px;
    font-family: "Montserrat", sans-serif;
    font-weight: 900;
    font-size: 112px;
    letter-spacing: -2px;
    color: var(--ink-black);
    line-height: 1;
  }
  .mascot-art {
    margin-top: 44px;
    width: 250px;
    height: 262px;
    border-radius: 46% 46% 40% 40%;
    background: radial-gradient(circle at 50% 40%, var(--can-red) 0%, var(--can-red-deep) 55%, var(--ink-black) 100%);
  }
  .tagline {
    margin-top: 46px;
    font-family: "Arimo", sans-serif;
    font-weight: 700;
    font-size: 25px;
    color: var(--can-red);
    text-align: center;
    line-height: 1.25;
  }
  .product-band {
    height: 64px;
    background: var(--can-red);
    display: flex;
    align-items: center;
    justify-content: center;
    font-family: "Arimo", sans-serif;
    font-weight: 700;
    font-size: 34px;
    color: var(--text-white);
    margin-bottom: 14px;
  }
</style>
</head>
<body>
  <main class="canvas">
    <section class="can-label">
      <div class="rim"></div>
      <header class="offer-band">
        <span class="offer-percent">33%</span>
        <span class="offer-word">FREE</span>
      </header>
      <div class="label-body">
        <h1 class="brand-name">6/40</h1>
        <div class="mascot-art" role="img" aria-label="Red and black elephant head mascot with white tusks"></div>
        <p class="tagline">ACTIVATE YOUR BODY<br>BE ACTIVE 6/40</p>
      </div>
      <footer class="product-band">ENERGY DRINK</footer>
      <div class="rim"></div>
    </section>
  </main>
</body>
</html>
```